Modernize Cleaning Chemical Product Labels

I am looking to modernise our product labels.
We are a cleaning chemical manufacture predominately in the commercial cleaning industry.
I would like for the labels to be available in at least 6 colours, red, green, blue, yellow, purple and orange.
Design can be as small as 270mm x 140mm up to 340mm x 165mm. Current label dimensions 275mm x 165mm
I have attached some of our current labels and our logo and also some competitors labels

Colors
0054AA
0677BA
7BADD7
CADEEF
E8F1F8
00AB8E
00BBA5
67D7C9
C6EFE9
E9F9F6
FFF300
FFF600
FEFA6F
FFFEC7
FFFEE8
F0912C
F2A743
F7CA91
FBE8D2
FDF5EE
EB3D1F
EC4F4E
F09395
F8D3D4
FCEDEE
A7469A
B969AE
D3A5CF
EDDBEB
F8F0F9

```html
<!DOCTYPE html>
<html lang="en">
<head>
<meta charset="utf-8">
<title>Brightline Premium Dishwashing Detergent – Label Range</title>
<link rel="stylesheet" href="https://fonts.googleapis.com/css2?family=Fira+Sans:wght@400;600;700;800&display=swap">
<style>
  :root {
    --teal: #1ba7c6;
    --teal-light: #35c3dd;
    --teal-dark: #1190ae;
    --white: #ffffff;
    --page: #f3f4f5;
    --green: #2a9a14;
    --green-deep: #0f5e1a;
    --blue: #0d3a8a;
    --blue-deep: #123f96;
    --purple: #8c1fa3;
    --purple-deep: #a52bb5;
  }
  * { box-sizing: border-box; margin: 0; padding: 0; }
  html, body { width: 1200px; height: 900px; overflow: hidden; }
  body {
    background: var(--page);
    font-family: "Fira Sans", sans-serif;
    display: flex;
    align-items: center;
    justify-content: center;
    gap: 30px;
  }
  .label {
    position: relative;
    width: 360px;
    height: 500px;
    border-radius: 10px;
    overflow: hidden;
    color: var(--white);
  }
  .label--green { --accent: var(--green); --accent-deep: var(--green-deep); }
  .label--blue { --accent: var(--blue); --accent-deep: var(--blue-deep); }
  .label--purple { --accent: var(--purple); --accent-deep: var(--purple-deep); }

  .label__shapes { position: absolute; inset: 0; }
  .label__shapes .accent { fill: var(--accent); }
  .label__shapes .teal { fill: var(--teal-dark); }

  .warning { position: absolute; left: 22px; top: 42px; }
  .warning__title { font-weight: 700; font-size: 15px; letter-spacing: 0.3px; }
  .warning__lines { margin-top: 10px; font-size: 8px; line-height: 1.25; text-transform: uppercase; }

  .product-name {
    position: absolute; left: 14px; top: 140px;
    font-weight: 800; font-size: 38px; letter-spacing: 0.5px;
    color: var(--accent-deep);
  }
  .details { position: absolute; left: 24px; top: 206px; right: 30px; }
  .details__title { font-weight: 800; font-size: 24px; line-height: 1.12; letter-spacing: 0.4px; }
  .details__claim { margin-top: 18px; font-weight: 700; font-size: 17px; letter-spacing: 0.3px; }
  .details__features { margin-top: 18px; font-weight: 600; font-size: 12.5px; line-height: 1.6; }

  .maker {
    position: absolute; left: 232px; top: 338px;
    border-left: 1px solid var(--white);
    padding-left: 7px;
    font-size: 7px; line-height: 1.45;
  }
  .volume {
    position: absolute; right: 42px; top: 386px;
    font-weight: 700; font-size: 28px; letter-spacing: 2px;
  }
</style>
</head>
<body>

  <article class="label label--green">
    <svg class="label__shapes" viewBox="0 0 360 500" aria-hidden="true">
      <defs>
        <linearGradient id="tealGreen" x1="0" y1="0" x2="1" y2="1">
          <stop offset="0" stop-color="#35c3dd"/><stop offset="1" stop-color="#1190ae"/>
        </linearGradient>
      </defs>
      <rect width="360" height="500" fill="url(#tealGreen)"/>
      <rect class="accent" x="0" y="128" width="265" height="6"/>
      <path class="accent" d="M0 190 H278 C300 250 316 290 340 300 V438 H0 Z"/>
      <rect x="0" y="438" width="360" height="4" fill="#35c3dd"/>
      <rect class="accent" x="0" y="446" width="340" height="54"/>
    </svg>
    <div class="warning">
      <p class="warning__title">WARNING</p>
      <p class="warning__lines">Not to be taken<br>Keep out of reach of children<br>Read safety directions before opening</p>
    </div>
    <h2 class="product-name">BRIGHTLINE</h2>
    <div class="details">
      <h3 class="details__title">PREMIUM<br>DISHWASHING<br>DETERGENT</h3>
      <p class="details__claim">BIODEGRADABLE</p>
      <p class="details__features">High Solids Content<br>Only 5 to 10mLs per 10L Wash<br>Grease and Oil Cutters + y<br>Coconut Oil Derivatives<br>Lemon Scented</p>
    </div>
    <p class="maker">Harlow Chemical Products<br>18 Wattle Park Rd.,<br>Marwood 4102. (07) 5550 1234</p>
    <p class="volume">5 L</p>
  </article>

  <article class="label label--blue">
    <svg class="label__shapes" viewBox="0 0 360 500" aria-hidden="true">
      <defs>
        <linearGradient id="tealBlue" x1="0" y1="0" x2="1" y2="1">
          <stop offset="0" stop-color="#35c3dd"/><stop offset="1" stop-color="#1190ae"/>
        </linearGradient>
      </defs>
      <rect width="360" height="500" fill="url(#tealBlue)"/>
      <rect class="accent" x="0" y="128" width="265" height="6"/>
      <path class="accent" d="M0 190 H278 C300 250 316 290 340 300 V438 H0 Z"/>
      <rect x="0" y="438" width="360" height="4" fill="#35c3dd"/>
      <rect class="accent" x="0" y="446" width="340" height="54"/>
    </svg>
    <div class="warning">
      <p class="warning__title">WARNING</p>
      <p class="warning__lines">Not to be taken<br>Keep out of reach of children<br>Read safety directions before opening</p>
    </div>
    <h2 class="product-name">BRIGHTLINE</h2>
    <div class="details">
      <h3 class="details__title">PREMIUM<br>DISHWASHING<br>DETERGENT</h3>
      <p class="details__claim">BIODEGRADABLE</p>
      <p class="details__features">High Solids Content<br>Only 5 to 10mLs per 10L Wash<br>Grease and Oil Cutters + y<br>Coconut Oil Derivatives<br>Lemon Scented</p>
    </div>
    <p class="maker">Harlow Chemical Products<br>18 Wattle Park Rd.,<br>Marwood 4102. (07) 5550 1234</p>
    <p class="volume">5 L</p>
  </article>

  <article class="label label--purple">
    <svg class="label__shapes" viewBox="0 0 360 500" aria-hidden="true">
      <defs>
        <linearGradient id="tealPurple" x1="0" y1="0" x2="1" y2="1">
          <stop offset="0" stop-color="#35c3dd"/><stop offset="1" stop-color="#1190ae"/>
        </linearGradient>
      </defs>
      <rect width="360" height="500" fill="url(#tealPurple)"/>
      <rect class="accent" x="0" y="128" width="265" height="6"/>
      <path class="accent" d="M0 190 H278 C300 250 316 290 340 300 V438 H0 Z"/>
      <rect x="0" y="438" width="360" height="4" fill="#35c3dd"/>
      <rect class="accent" x="0" y="446" width="340" height="54"/>
    </svg>
    <div class="warning">
      <p class="warning__title">WARNING</p>
      <p class="warning__lines">Not to be taken<br>Keep out of reach of children<br>Read safety directions before opening</p>
    </div>
    <h2 class="product-name">BRIGHTLINE</h2>
    <div class="details">
      <h3 class="details__title">PREMIUM<br>DISHWASHING<br>DETERGENT</h3>
      <p class="details__claim">BIODEGRADABLE</p>
      <p class="details__features">High Solids Content<br>Only 5 to 10mLs per 10L Wash<br>Grease and Oil Cutters + y<br>Coconut Oil Derivatives<br>Lemon Scented</p>
    </div>
    <p class="maker">Harlow Chemical Products<br>18 Wattle Park Rd.,<br>Marwood 4102. (07) 5550 1234</p>
    <p class="volume">5 L</p>
  </article>

</body>
</html>
```